Minimalist Sign Design (24” X 24”)

I am wanting to redesign our yard signs to be very clean, attractive, eye catching, and readable (imagine driving by a home with a sign In yard). We paint homes. I am hoping to have a design that incorporates our brand colors in a clean, professional way that represents our company. Clean, concise, easily read from a distance.

Target Market(s)

Homeowners

Industry/Entity Type

Painting And Decorating

Font styles to use
Sans Serif

Requirements
Must have
• Phone Number: (555) 014-7391
• Free Consultations
• Makeover in progress!
• Brand colors:
• Hunter Green: #355e3b
• Black
• White
Nice to have
• Would like the hunter green to he background color of sign. Can make logo white to stand out with the green.
Should not have
• Too busy or unable to read text

```html
<!DOCTYPE html>
<html lang="en">
<head>
<meta charset="utf-8">
<title>Keystone Painting Yard Sign</title>
<link rel="stylesheet" href="https://fonts.googleapis.com/css2?family=Poppins:wght@300;400&family=Noto+Serif:wght@400&display=swap">
<style>
  :root {
    --hunter-green: #36613e;
    --white: #ffffff;
  }
  html, body {
    margin: 0;
    padding: 0;
    width: 1200px;
    height: 1200px;
    overflow: hidden;
    background: var(--hunter-green);
  }
  .sign {
    position: relative;
    width: 1200px;
    height: 1200px;
    background: var(--hunter-green);
    color: var(--white);
  }
  .brand {
    position: absolute;
    top: 150px;
    left: 0;
    width: 100%;
    text-align: center;
    font-family: "Poppins", sans-serif;
    font-weight: 400;
    font-size: 40px;
    line-height: 1.3;
    letter-spacing: 0.22em;
    color: var(--white);
  }
  .brand-name {
    display: block;
  }
  .phone-band {
    position: absolute;
    top: 458px;
    left: 0;
    width: 100%;
    height: 174px;
    background: var(--white);
    display: flex;
    align-items: center;
    justify-content: center;
  }
  .phone-number {
    font-family: "Noto Serif", serif;
    font-weight: 400;
    font-size: 128px;
    letter-spacing: 0.02em;
    color: var(--hunter-green);
    line-height: 1;
    margin-top: -6px;
  }
  .offer {
    position: absolute;
    top: 764px;
    left: 0;
    width: 100%;
    text-align: center;
    font-family: "Poppins", sans-serif;
    font-weight: 300;
    font-size: 82px;
    line-height: 1.2;
    color: var(--white);
    margin: 0;
  }
  .tagline {
    position: absolute;
    top: 912px;
    left: 149px;
    width: 902px;
    display: flex;
    align-items: center;
    gap: 18px;
  }
  .tagline-rule {
    flex: 1;
    height: 2px;
    background: var(--white);
  }
  .tagline-text {
    font-family: "Noto Serif", serif;
    font-weight: 400;
    font-size: 33px;
    letter-spacing: 0.1em;
    color: var(--white);
    white-space: nowrap;
    line-height: 1.4;
  }
</style>
</head>
<body>
  <main class="sign">
    <div class="brand">
      <span class="brand-name">KEYSTONE</span>
      <span class="brand-name">PAINTING</span>
    </div>
    <div class="phone-band">
      <span class="phone-number">(555) 014-7391</span>
    </div>
    <h1 class="offer">FREE CONSULTATIONS</h1>
    <div class="tagline">
      <span class="tagline-rule"></span>
      <span class="tagline-text">MAKEOVER IN PROGRESS!</span>
      <span class="tagline-rule"></span>
    </div>
  </main>
</body>
</html>
```